Plumbing Service Flyer Needed For Swapboard

Plumbing ad needs to be effective (600 by 450 pixels)
Ad must include company name Plumbing Aces and phone number 202-555-0187
No URLs, links, or web addresses in your text or image please.

(about us we offer a wide range of plumbing services from emergency plumbing to commercial plumbing services, our master plumbers are ready to handle all jobs, large or small, at anytime during the day or night. Pickup the phone and call us today).

Target Market(s)

DC Metro Area

Industry/Entity Type

Plumbing

Font styles to use
Other font styles liked:
• No preference. Let the designer choose

Colors

Designer to choose colors to be used in the design.

Requirements
Must have
• 1. A bold headline: headline should communicate what my business is all about.
• 2. Great photography
• 3. Discounts or specials
• 4. Call to action
• 5. Key facts: Let consumers know about the product or service (see attached ad)
• 6. Good graphics
Should not have
• No URLs, links, or web addresses in your text or image please.

```html
<!DOCTYPE html>
<html lang="en">
<head>
<meta charset="utf-8">
<title>Plumbing Aces Flyer</title>
<link href="https://fonts.googleapis.com/css2?family=Oswald:wght@600;700&family=Open+Sans:wght@400&display=swap" rel="stylesheet">
<style>
  :root {
    --brand-blue: #2a66a8;
    --brand-yellow: #f7d416;
    --ink: #111111;
    --wood-dark: #7a4b26;
    --wood-light: #a8703f;
    --panel: rgba(250, 248, 244, 0.9);
    --white: #ffffff;
    --bullet: #2a66a8;
  }
  html, body {
    margin: 0;
    padding: 0;
    width: 1200px;
    height: 840px;
    overflow: hidden;
    background: #ffffff;
  }
  .flyer {
    position: relative;
    width: 1200px;
    height: 840px;
    overflow: hidden;
    background: linear-gradient(100deg, var(--wood-dark), var(--wood-light) 45%, var(--wood-dark) 80%, var(--wood-light));
    font-family: "Open Sans", Arial, sans-serif;
  }
  .side-column {
    position: absolute;
    left: 20px;
    top: 0;
    width: 392px;
    height: 840px;
    background: var(--brand-yellow);
  }
  .brand-band {
    position: absolute;
    left: 0;
    top: 18px;
    width: 429px;
    height: 101px;
    background: var(--brand-blue);
    display: flex;
    align-items: center;
    justify-content: center;
  }
  .brand-name {
    margin: 0;
    font-family: "Oswald", Impact, sans-serif;
    font-weight: 700;
    font-size: 54px;
    color: var(--white);
    letter-spacing: 0.5px;
    padding-left: 20px;
  }
  .headline {
    position: absolute;
    left: 20px;
    top: 140px;
    width: 392px;
    margin: 0;
    text-align: center;
    font-family: "Oswald", Impact, sans-serif;
    font-weight: 700;
    text-transform: uppercase;
  }
  .headline-lead {
    display: block;
    font-size: 29px;
    line-height: 34px;
    color: var(--ink);
  }
  .headline-main {
    display: block;
    font-size: 80px;
    line-height: 70px;
    color: var(--brand-blue);
    margin-top: 4px;
  }
  .photo-plumber {
    position: absolute;
    left: 45px;
    top: 320px;
    width: 346px;
    height: 520px;
    background: linear-gradient(180deg, #2b3345 0%, #1c2230 60%, #141925 100%);
    border-radius: 140px 140px 0 0;
  }
  .photo-team {
    position: absolute;
    left: 412px;
    top: 0;
    width: 788px;
    height: 274px;
    background: linear-gradient(120deg, #27527f 0%, #3c6e9e 45%, #6d93b8 75%, #9fb4c6 100%);
    border-bottom: 5px solid var(--white);
  }
  .content-panel {
    position: absolute;
    left: 446px;
    top: 282px;
    width: 722px;
    height: 478px;
    background: var(--panel);
    border-radius: 0 0 14px 14px;
  }
  .intro {
    position: absolute;
    left: 470px;
    top: 292px;
    width: 674px;
    margin: 0;
    font-size: 17px;
    line-height: 22.5px;
    color: var(--ink);
    text-align: justify;
    text-align-last: center;
  }
  .promise-box {
    position: absolute;
    left: 434px;
    top: 402px;
    width: 320px;
    height: 332px;
    box-sizing: border-box;
    padding: 22px 30px 0 34px;
    background: var(--brand-blue);
    border-radius: 4px 12px 12px 12px;
  }
  .promise-box p {
    margin: 0;
    color: var(--white);
    font-size: 16.5px;
    line-height: 22.6px;
    text-align: justify;
  }
  .services {
    position: absolute;
    left: 784px;
    top: 424px;
    width: 360px;
    color: var(--ink);
  }
  .services-title {
    margin: 0 0 18px;
    font-size: 17px;
    font-weight: 400;
  }
  .services-list {
    list-style: none;
    margin: 0;
    padding: 0 0 0 14px;
  }
  .services-list li {
    position: relative;
    padding-left: 16px;
    font-size: 17px;
    line-height: 19px;
    margin-bottom: 7px;
  }
  .services-list li::before {
    content: "";
    position: absolute;
    left: 0;
    top: 6px;
    width: 9px;
    height: 9px;
    border-radius: 50%;
    background: var(--bullet);
  }
  .phone-tab {
    position: absolute;
    left: 642px;
    top: 770px;
    width: 330px;
    height: 70px;
    background: var(--brand-yellow);
    border-radius: 10px 10px 0 0;
    display: flex;
    align-items: center;
    justify-content: center;
  }
  .phone-number {
    font-family: "Oswald", Impact, sans-serif;
    font-weight: 700;
    font-size: 38px;
    color: var(--ink);
    letter-spacing: 0.5px;
  }
</style>
</head>
<body>
<main class="flyer">
  <div class="side-column"></div>
  <div class="brand-band"><h1 class="brand-name">PLUMBING ACES</h1></div>
  <h2 class="headline">
    <span class="headline-lead">We have all experienced a</span>
    <span class="headline-main">Plumbing<br>Emergency</span>
  </h2>
  <div class="photo-plumber" role="img" aria-label="Smiling plumber in navy overalls and cap, arms crossed, holding a red pipe wrench"></div>

  <div class="photo-team" role="img" aria-label="Two plumbers in blue shirts working on a chrome faucet beside an open blue toolbox"></div>

  <div class="content-panel"></div>
  <p class="intro">we offer a wide range of plumbing services from emergency plumbing to commercial plumbing services, our master plumbers are ready to handle all jobs, large or small, at anytime during the day or night. Pickup the phone and call us today.</p>

  <div class="promise-box">
    <p>24/7 plumber at your service! The best priced any plumbing repair install or remodel. You only need one call for us to handle it all, super fast, always reliable &amp; affordable plumber. Call us today for same day service. Bonded, licensed and insured. We handle fixes, installation, leaks, remodels, new construction and more! do not use a handyman, use a certified plumber like me.</p>
  </div>

  <section class="services">
    <h3 class="services-title">Here are a few of my plumbing services:</h3>
    <ul class="services-list">
      <li>Plumbing clogs</li>
      <li>Water heater replacement</li>
      <li>Repair and install gas lines</li>
      <li>Remodel your plumbing</li>
      <li>Flood repair</li>
      <li>Disposals repair and install</li>
      <li>Toilets install or replace</li>
      <li>New piping and repairs</li>
      <li>New homes, old homes, commercial plumbing and a ton more</li>
    </ul>
  </section>

  <div class="phone-tab"><span class="phone-number">202-555-0187</span></div>
</main>
</body>
</html>
```